Looking for fresh and exciting business card design that is simple and yet eye catching and impactfu

I am starting my own independent Marketing Communications consultancy with aim to service a small group of clients. Focus on aviation, travel and hospitality industries. Name of the consultancy is RQB BizLink or RQB Marketing Communications. Basic content of the card will be
RQB Marketing Communications / RQB BizLink
Greta Lund Okafor
Email
Mobile
Website

Target Market(s)

Aviation, travel and hospitality industries

Industry/Entity Type

Travel

Contact Information for Business Card

Greta Lund Okafor
Consultant
gretalok@mailbrook.example
Mobile : +86 1529 804 2617
Skype: gretabluepebble

Font styles to use
Sans Serif
Script

Requirements
Must have
• Professional look and feel.
Nice to have
• Fresh, contrast. I don't have a logo so using the company name to create a focal point.
Should not have
• Too many colors.

```html
<!DOCTYPE html>
<html lang="en">
<head>
<meta charset="utf-8">
<title>RQB Marketing Communications – Business Card</title>
<link rel="stylesheet" href="https://fonts.googleapis.com/css2?family=Arimo:wght@400;700&display=swap">
<style>
  :root {
    --page-bg: #e4e5e6;
    --card-slate: #6f8690;
    --card-slate-dark: #637a85;
    --band-light: #dfe3e4;
    --band-edge: #c9cfd1;
    --text-white: #f4f7f8;
    --text-dark: #111417;
    --globe-light: #6fb4ea;
    --globe-dark: #123f86;
    --rule-dots: #e8eef0;
  }
  * { margin: 0; padding: 0; box-sizing: border-box; }
  html, body {
    width: 1200px; height: 1200px; overflow: hidden;
    background: var(--page-bg);
    font-family: "Arimo", Arial, sans-serif;
  }
  .sheet {
    width: 1200px; height: 1200px;
    display: flex; flex-direction: column; align-items: center; justify-content: center;
    gap: 52px;
  }
  .card {
    position: relative;
    width: 900px; height: 514px;
    background: radial-gradient(ellipse at 60% 45%, var(--card-slate) 0%, var(--card-slate-dark) 100%);
    box-shadow: 0 6px 18px rgba(0,0,0,0.18);
    overflow: hidden;
  }
  .card-front { border: 12px solid var(--band-light); }
  .brand-mark {
    position: absolute; left: 0; right: 0; top: 150px;
    text-align: center;
  }
  .brand-name {
    font-size: 150px; font-weight: 700; letter-spacing: 2px;
    color: var(--text-white); line-height: 1;
  }
  .brand-tagline {
    margin-top: 6px;
    font-size: 34px; font-weight: 700; color: var(--text-dark);
  }
  .card-shapes { position: absolute; inset: 0; }
  .back-brand {
    position: absolute; left: 60px; top: 60px; width: 360px; text-align: center;
    color: var(--text-white); font-weight: 700;
  }
  .back-brand .brand-name-small { font-size: 56px; line-height: 1; }
  .back-brand .brand-tagline-small { font-size: 22px; margin-top: 4px; }
  .holder {
    position: absolute; left: 520px; top: 150px; color: var(--text-white);
  }
  .holder-name { font-size: 40px; font-weight: 400; }
  .holder-role {
    margin-left: 110px; font-size: 18px; font-weight: 700; color: var(--text-dark);
    letter-spacing: 0.5px;
  }
  .contact-list {
    position: absolute; left: 530px; top: 262px; list-style: none;
    color: var(--text-white); font-size: 20px;
  }
  .contact-item { display: flex; align-items: center; gap: 14px; height: 40px; }
  .contact-icon { width: 24px; height: 24px; flex: none; }
</style>
</head>
<body>
<main class="sheet">

  <section class="card card-front" aria-label="Card front">
    <div class="brand-mark">
      <div class="brand-name">RQB</div>
      <div class="brand-tagline">Marketing Communications</div>
    </div>
  </section>

  <section class="card card-back" aria-label="Card back">
    <svg class="card-shapes" width="900" height="514" viewBox="0 0 900 514">
      <polygon points="0,0 900,0 900,514 0,514 0,0 14,14 14,500 886,500 886,14 14,14" fill="var(--band-light)" fill-rule="evenodd"/>
      <polygon points="650,14 886,14 886,60 690,60" fill="var(--band-light)"/>
      <polygon points="14,454 200,454 240,500 14,500" fill="var(--band-light)"/>
      <line x1="462" y1="40" x2="462" y2="470" stroke="var(--rule-dots)" stroke-width="2" stroke-dasharray="2 6"/>
      <line x1="480" y1="230" x2="870" y2="230" stroke="var(--rule-dots)" stroke-width="2" stroke-dasharray="2 6"/>
      <line x1="170" y1="158" x2="310" y2="158" stroke="var(--rule-dots)" stroke-width="2" stroke-dasharray="2 5"/>
      <defs>
        <radialGradient id="globeTone" cx="40%" cy="35%" r="70%">
          <stop offset="0%" stop-color="var(--globe-light)"/>
          <stop offset="100%" stop-color="var(--globe-dark)"/>
        </radialGradient>
      </defs>
      <circle cx="240" cy="270" r="64" fill="#d9dde0"/>
      <circle cx="240" cy="270" r="56" fill="url(#globeTone)" role="img" aria-label="Blue world globe illustration"/>
    </svg>

    <div class="back-brand">
      <div class="brand-name-small">RQB</div>
      <div class="brand-tagline-small">Marketing Communications</div>
    </div>

    <div class="holder">
      <div class="holder-name">Greta Lund Okafor</div>
      <div class="holder-role">CONSULTAN</div>
    </div>

    <ul class="contact-list">
      <li class="contact-item">
        <svg class="contact-icon" viewBox="0 0 24 24" aria-hidden="true">
          <circle cx="12" cy="8" r="5" fill="#d4dadc"/>
          <path d="M3 22c0-5 4-8 9-8s9 3 9 8z" fill="#d4dadc"/>
        </svg>
        <span>+86 1529 804 2617</span>
      </li>
      <li class="contact-item">
        <svg class="contact-icon" viewBox="0 0 24 24" aria-hidden="true">
          <circle cx="12" cy="12" r="10" fill="#d4dadc"/>
        </svg>
        <span>gretabluepebble</span>
      </li>
      <li class="contact-item">
        <svg class="contact-icon" viewBox="0 0 24 24" aria-hidden="true">
          <rect x="2" y="5" width="20" height="14" fill="#d4dadc"/>
          <path d="M2 5l10 8 10-8" fill="none" stroke="#7a8c94" stroke-width="1.5"/>
        </svg>
        <span>gretalok@mailbrook.example</span>
      </li>
    </ul>
  </section>

</main>
</body>
</html>
```